Business Card

The design you sent was fine. I just need the logo changed on one side. The back needs to have the text "Vell Marrow Group" next to the log and the words "Insight Integrity Impact" in the middle. The front logo needs to have the "Vell Marrow Advisory" logo attached

Colors

Designer to choose colors to be used in the design.

```html
<!DOCTYPE html>
<html lang="en">
<head>
<meta charset="utf-8">
<title>Vell Marrow — Business Card</title>
<link href="https://fonts.googleapis.com/css2?family=Open+Sans:wght@400;600&family=Arimo:wght@400&display=swap" rel="stylesheet">
<style>
  :root {
    --bg: #0a0a0b;
    --card: #2a2b2d;
    --edge: #19b4e3;
    --accent: #1cb6e6;
    --ink: #f2f2f2;
    --ink-soft: #d9d9d9;
  }
  * { margin: 0; padding: 0; box-sizing: border-box; }
  html, body { width: 1200px; height: 822px; overflow: hidden; background: var(--bg); }
  .stage {
    width: 1200px; height: 822px;
    display: flex; align-items: center; justify-content: center; gap: 60px;
  }
  .card {
    width: 500px; height: 286px;
    background: var(--card);
    border: 2px solid var(--edge);
    border-radius: 3px;
    position: relative;
  }

  /* Front: contact side */
  .card--front { padding: 34px 40px; }
  .brand { display: flex; align-items: center; gap: 14px; }
  .brand__mark {
    width: 40px; height: 40px; border-radius: 50%;
    background: var(--accent); flex: none; margin: 0 3px;
  }
  .brand__name {
    font-family: "Open Sans", sans-serif; font-weight: 600;
    font-size: 30px; color: var(--ink); line-height: 1.05; letter-spacing: 0.2px;
    white-space: nowrap;
  }
  .brand__tagline {
    font-family: "Open Sans", sans-serif; font-size: 8px; color: var(--ink-soft);
    margin: 6px 0 0 60px; letter-spacing: 0.3px;
  }
  .person { margin: 22px 0 0 60px; font-family: "Arimo", sans-serif; }
  .person__name { color: var(--accent); font-size: 21px; line-height: 1.1; }
  .person__role { color: var(--ink); font-size: 14px; margin-top: 2px; }
  .contact {
    margin: 14px 0 0 60px; font-family: "Arimo", sans-serif;
    color: var(--ink); font-size: 13.5px; line-height: 1.4;
  }
  .contact__label { color: var(--accent); }
  .contact__web { color: var(--accent); }

  /* Back: brand side */
  .card--back { display: flex; align-items: center; justify-content: center; }
  .back-brand { display: flex; align-items: center; gap: 16px; }
  .back-brand__mark {
    width: 48px; height: 48px; border-radius: 50%;
    background: var(--accent); flex: none;
  }
  .back-brand__name {
    font-family: "Open Sans", sans-serif; font-weight: 600;
    font-size: 30px; color: var(--ink); line-height: 1; white-space: nowrap;
  }
  .back-brand__tagline {
    font-family: "Open Sans", sans-serif; font-size: 12px; color: var(--ink);
    margin-top: 8px; text-align: center; letter-spacing: 0.2px;
  }
</style>
</head>
<body>
<main class="stage">
  <section class="card card--front" aria-label="Business card front">
    <div class="brand">
      <span class="brand__mark"></span>
      <span class="brand__name">Vell Marrow Advisory</span>
    </div>
    <p class="brand__tagline">Clear Thinking delivering Lasting Results</p>
    <div class="person">
      <p class="person__name">Daniel Hartwell</p>
      <p class="person__role">Managing Director</p>
    </div>
    <div class="contact">
      <p>27, Harbour Lane Studios</p>
      <p>Eastmere, 604218.</p>
      <p><span class="contact__label">P:</span> 055-246 810 357 | <span class="contact__label">E:</span> hello@vellmarrow.com</p>
      <p class="contact__web">www.vellmarrow.com</p>
    </div>
  </section>

  <section class="card card--back" aria-label="Business card back">
    <div>
      <div class="back-brand">
        <span class="back-brand__mark"></span>
        <span class="back-brand__name">Vell Marrow Group</span>
      </div>
      <p class="back-brand__tagline">Insight Integrity Impact</p>
    </div>
  </section>
</main>
</body>
</html>
```